job report

Designer – Professional Plumbing Job Report Template

Overview

We are seeking a skilled designer to create a professional, easy-to-use Job Report template for a commercial and maintenance plumbing business.
The report will be used for clients, property managers, facilities managers, strata, and retail centres and must clearly communicate findings, works completed, and recommendations in a polished, compliant, and branded format.

The final document must be suitable for PDF delivery, email, and ongoing reuse.

Objectives

Present plumbing works in a clear, professional, and defensible report format

Improve client understanding of findings and recommendations

Provide a repeatable template that can be used across maintenance, reactive, and investigative works

Allow easy insertion of text, tables, and photos

Report Structure (Minimum Inclusions)
1. Cover Page

Company logo and branding

Report title (e.g. Plumbing Job Report / Investigation Report)

Client name

Site address

Job reference / work order number

Date of attendance

Technician / contractor name

2. Client & Site Details

Client / company name

Site address

Contact person

Contact details

Access notes (after-hours, tenant access, etc.)

3. Reason for Attendance

Clear description of why attendance was required

Call-out type (reactive, scheduled maintenance, investigation, emergency, etc.)

Reported issue or scope requested by client

4. Findings / Observations

Detailed findings discovered on site

Condition of pipework, fixtures, drainage, or systems

Any contributing factors identified

Notes on compliance, wear, damage, or risk

(This section should support bullet points and paragraphs.)

5. Works Carried Out

Step-by-step description of works completed

Equipment used (e.g. jetter, CCTV camera, leak detection, flex shaft, etc.)

Repairs, replacements, testing, and verification

Confirmation that systems were tested and operational on completion

6. Photos & Visual Evidence

Clearly labelled photo sections

Before / during / after photos

Space for photo captions and explanations

Logical layout that aligns photos with written findings

7. Recommendations

Clearly separated from works completed

Urgent vs non-urgent recommendations

Preventative maintenance advice

Upgrade or replacement suggestions

Risk-based language where appropriate

8. Limitations & Exclusions

Areas not inspected

Access limitations

Assumptions made during inspection

Items outside scope of works

9. Conclusion

Summary of outcome

Confirmation of current system status

Next steps (if any)

10. Sign-Off

Contractor / technician name

Company name

Date

Optional client acknowledgement section

Design Requirements

Clean, professional layout

Commercial / trade-appropriate styling (not overly creative)

Easy-to-read fonts

Consistent headings and spacing

Logical flow for busy property managers

Editable format (Word / Google Docs / InDesign source file)

Final export-ready PDF version

Bonus (Nice to Have)

Traffic-light system (Green / Amber / Red) for condition reporting

Iconography for findings, repairs, and recommendations

Optional sections for compliance notes (AS/NCC references)

Space for QR codes or job reference numbers

Deliverables

Editable master report template

PDF version

Instructions or notes for ongoing use

```html
<!DOCTYPE html>
<html lang="en">
<head>
<meta charset="UTF-8">
<title>Plumbing Job Report – Recommendations to Sign-Off</title>
<link rel="stylesheet" href="https://fonts.googleapis.com/css2?family=Questrial&family=Poppins:wght@600&display=swap">
<style>
  :root {
    --paper: #f1f2f4;
    --paper-shade: #e4e6ea;
    --ink: #1c1c1c;
    --rule: #2a2a2a;
    --accent-cyan: #5ff0fb;
    --accent-yellow: #ffff00;
  }
  * { box-sizing: border-box; margin: 0; padding: 0; }
  html, body { width: 856px; height: 1200px; overflow: hidden; background: var(--paper); }
  .sheet {
    position: relative;
    width: 856px;
    height: 1200px;
    overflow: hidden;
    font-family: "Questrial", "Century Gothic", sans-serif;
    color: var(--ink);
  }
  .backdrop {
    position: absolute;
    inset: 0;
    background: linear-gradient(160deg, #f4f5f7 0%, var(--paper) 45%, var(--paper-shade) 100%);
  }
  .section-head {
    position: absolute;
    left: 52px;
    width: 752px;
    height: 22px;
  }
  .section-head svg { position: absolute; left: 0; top: 0; }
  .section-title {
    position: relative;
    display: block;
    padding-left: 6px;
    font-family: "Poppins", sans-serif;
    font-weight: 600;
    font-size: 16px;
    line-height: 22px;
    color: #0f0f0f;
  }
  .field {
    position: absolute;
    left: 52px;
    width: 752px;
  }
  .row {
    display: flex;
    align-items: flex-end;
    height: 28px;
  }
  .label {
    font-size: 15.5px;
    line-height: 1;
    padding-bottom: 3px;
    white-space: nowrap;
    margin-right: 7px;
    letter-spacing: -0.1px;
  }
  .rule {
    flex: 1;
    border-bottom: 1px solid var(--rule);
  }
  .row.split .rule.company { flex: 0 0 377px; }
  .row.split .label.date { margin-left: 7px; }
</style>
</head>
<body>
<main class="sheet">
  <div class="backdrop" role="img" aria-label="Faint background of plumbing tools: spanners, bolts, nuts and screws"></div>

  <!-- Recommendations -->
  <div class="section-head" style="top:51px">
    <svg width="752" height="22" viewBox="0 0 752 22" aria-hidden="true">
      <polygon points="0,0 177,0 191,21 0,21" fill="var(--accent-cyan)"/>
      <polygon points="177,0 230,0 247,21 191,21" fill="var(--accent-yellow)"/>
      <rect x="0" y="19" width="752" height="2.5" fill="var(--accent-cyan)"/>
    </svg>
    <span class="section-title">Recommendations</span>
  </div>
  <div class="field" style="top:73px">
    <div class="row"><span class="label">Urgent Recommendations:</span><span class="rule"></span></div>
    <div class="row"><span class="rule"></span></div>
    <div class="row"><span class="rule"></span></div>
  </div>
  <div class="field" style="top:156px">
    <div class="row"><span class="label">Non-Urgent Recommendations:</span><span class="rule"></span></div>
    <div class="row"><span class="rule"></span></div>
    <div class="row"><span class="rule"></span></div>
  </div>
  <div class="field" style="top:240px">
    <div class="row"><span class="label">Preventative maintenance advice:</span><span class="rule"></span></div>
    <div class="row"><span class="rule"></span></div>
    <div class="row"><span class="rule"></span></div>
  </div>
  <div class="field" style="top:323px">
    <div class="row"><span class="label">Upgrade or replacement suggestions:</span><span class="rule"></span></div>
    <div class="row"><span class="rule"></span></div>
    <div class="row"><span class="rule"></span></div>
  </div>
  <div class="field" style="top:407px">
    <div class="row"><span class="label">Risk-based language where appropriate:</span><span class="rule"></span></div>
    <div class="row"><span class="rule"></span></div>
    <div class="row"><span class="rule"></span></div>
  </div>

  <!-- Limitations & Exclusions -->
  <div class="section-head" style="top:505px">
    <svg width="752" height="22" viewBox="0 0 752 22" aria-hidden="true">
      <polygon points="0,0 205,0 219,21 0,21" fill="var(--accent-cyan)"/>
      <polygon points="205,0 258,0 275,21 219,21" fill="var(--accent-yellow)"/>
      <rect x="0" y="19" width="752" height="2.5" fill="var(--accent-cyan)"/>
    </svg>
    <span class="section-title" style="padding-left:9px">Limitations &amp; Exclusions</span>
  </div>
  <div class="field" style="top:526px">
    <div class="row"><span class="label">Areas not inspected:</span><span class="rule"></span></div>
    <div class="row"><span class="rule"></span></div>
    <div class="row"><span class="rule"></span></div>
  </div>
  <div class="field" style="top:610px">
    <div class="row"><span class="label">Access limitations:</span><span class="rule"></span></div>
    <div class="row"><span class="rule"></span></div>
    <div class="row"><span class="rule"></span></div>
  </div>
  <div class="field" style="top:693px">
    <div class="row"><span class="label">Assumptions made during inspection:</span><span class="rule"></span></div>
    <div class="row"><span class="rule"></span></div>
    <div class="row"><span class="rule"></span></div>
  </div>
  <div class="field" style="top:777px">
    <div class="row"><span class="label">Items outside scope of works:</span><span class="rule"></span></div>
    <div class="row"><span class="rule"></span></div>
    <div class="row"><span class="rule"></span></div>
  </div>

  <!-- Conclusion -->
  <div class="section-head" style="top:876px">
    <svg width="752" height="22" viewBox="0 0 752 22" aria-hidden="true">
      <polygon points="0,0 120,0 134,21 0,21" fill="var(--accent-cyan)"/>
      <polygon points="120,0 173,0 190,21 134,21" fill="var(--accent-yellow)"/>
      <rect x="0" y="19" width="752" height="2.5" fill="var(--accent-cyan)"/>
    </svg>
    <span class="section-title" style="padding-left:9px">Conclusion</span>
  </div>
  <div class="field" style="top:897px">
    <div class="row"><span class="label">Summary of outcome:</span><span class="rule"></span></div>
    <div class="row"><span class="rule"></span></div>
  </div>
  <div class="field" style="top:953px">
    <div class="row"><span class="label">Confirmation of current system status:</span><span class="rule"></span></div>
    <div class="row"><span class="rule"></span></div>
  </div>
  <div class="field" style="top:1008px">
    <div class="row"><span class="label">Next steps (if any):</span><span class="rule"></span></div>
    <div class="row"><span class="rule"></span></div>
  </div>

  <!-- Sign-Off -->
  <div class="section-head" style="top:1079px">
    <svg width="752" height="22" viewBox="0 0 752 22" aria-hidden="true">
      <polygon points="0,0 92,0 106,21 0,21" fill="var(--accent-cyan)"/>
      <polygon points="92,0 145,0 162,21 106,21" fill="var(--accent-yellow)"/>
      <rect x="0" y="19" width="752" height="2.5" fill="var(--accent-cyan)"/>
    </svg>
    <span class="section-title" style="padding-left:9px">Sign-Off</span>
  </div>
  <div class="field" style="top:1100px">
    <div class="row"><span class="label">Contractor / Technician name:</span><span class="rule"></span></div>
    <div class="row split"><span class="label">Company name:</span><span class="rule company"></span><span class="label date">Date:</span><span class="rule"></span></div>
  </div>
</main>
</body>
</html>
```